Corvane Collective Web Presence Design and Relaunch

Take existing web files and "clean up" for a a more presentable web landing pad.
posted presently on a site pad CSS template. at www.corvanecollective.org

The site is clunky and unprofessional looking. Needs to be toned down so the urgency is conveyed, but not via a burning planet image.

Target Market(s)

Non-profit climate adaptation group targeting local government land management agencies, special districts and private landholders of natural resource properties.

Industry/Entity Type

Environment

Coding

Coded - Design and coding required

Number of Pages Required

4 page

Font styles to use
Serif
Sans Serif

Requirements
Must have
• Include current logos, aspects if content on current site www.corvanecollective.org
• A regional Pacific Northwest Focus (US & Canada). Content speaking to urgency but respectful of cultural diversity and norms. Sustainability themes. Emphasis on action and implementation.
Nice to have
• link to like minded projects. Appear to future generations. Diversity in thematic areas ecological resiliency, energy, food security and infrastructure.

```html
<!DOCTYPE html>
<html lang="en">
<head>
<meta charset="utf-8">
<title>Corvane Collective — Climate Adaptation</title>
<link rel="stylesheet" href="https://fonts.googleapis.com/css2?family=Alegreya:wght@400;500&family=Oswald:wght@500&family=Poppins:wght@400;500&display=swap">
<style>
:root{
  --green:#a5cf4c;
  --blue:#1a8fc9;
  --ink:#2a2a2a;
  --muted:#6b6b6b;
  --white:#ffffff;
  --sans:'Poppins',sans-serif;
  --serif:'Alegreya',serif;
}
*{margin:0;padding:0;box-sizing:border-box}
html,body{width:1200px;height:4219px;overflow:hidden}
body{position:relative;background:var(--white);font-family:var(--sans);color:var(--ink)}
.abs{position:absolute}
.btn{position:absolute;display:flex;align-items:center;justify-content:center;font-family:var(--serif);font-size:20px;letter-spacing:.5px;color:var(--white);text-transform:uppercase;text-decoration:none}
.btn-green{background:var(--green)}
.btn-blue{background:var(--blue)}
.section-title{position:absolute;left:0;width:1200px;text-align:center;font-family:var(--serif);font-size:44px;color:var(--blue);font-weight:500}

/* top bar */
.topbar{left:0;top:0;width:1200px;height:41px;background:var(--green)}
.social{display:flex;gap:4px}
.social span{width:30px;height:30px;border-radius:50%;display:block}
.topbar .social{position:absolute;left:76px;top:5px}
.s1{background:#3b5998}.s2{background:#c9412f}.s3{background:#1da1f2}.s4{background:#b8312f}.s5{background:#e8772e}
.call{position:absolute;right:86px;top:5px;display:flex;align-items:center;gap:10px;color:var(--white);font-size:14px}
.call .ring{width:30px;height:30px;border-radius:50%;background:var(--blue);display:flex;align-items:center;justify-content:center}
.call b{font-family:var(--serif);font-weight:400;font-size:18px}

/* nav */
.nav{left:0;top:41px;width:1200px;height:83px;background:var(--white)}
.nav a{position:absolute;top:33px;font-size:14px;color:var(--ink);text-decoration:none}
.nav a.active{color:var(--blue);border-bottom:2px solid var(--blue);padding-bottom:2px}
.brand{position:absolute;display:flex;flex-direction:column;align-items:center;gap:5px}
.brand .dot{width:34px;height:34px;border-radius:50%;background:var(--green)}
.brand .name{font-family:var(--sans);font-weight:500;color:var(--green);font-size:11px;letter-spacing:1px;white-space:nowrap}

/* hero */
.hero{left:0;top:124px;width:1200px;height:552px;background:linear-gradient(180deg,#7e8b80 0%,#67734f 100%)}
.hero .kicker{position:absolute;top:206px;width:1200px;text-align:center;color:var(--white);font-size:25px;font-weight:500}
.hero h1{position:absolute;top:245px;width:1200px;text-align:center;font-family:'Oswald',sans-serif;font-weight:500;font-size:58px;color:var(--white)}
.arrow{position:absolute;top:238px;width:48px;height:48px;border-radius:50%;border:2px solid rgba(255,255,255,.8)}

/* doing */
.intro{left:295px;top:1148px;width:610px;text-align:center;font-size:14px;line-height:27px;color:var(--muted)}

/* split */
.split-photo{left:0;top:1405px;width:600px;height:415px;background:linear-gradient(180deg,#5f7a44,#3d5230)}
.split-panel{left:600px;top:1405px;width:600px;height:415px;background:var(--green)}
.tab{position:absolute;left:403px;width:301px;height:55px;display:flex;align-items:center;padding-left:40px;font-family:var(--serif);font-size:21px;background:var(--white);color:var(--ink)}
.tab.active{background:var(--green);color:var(--white)}
.split-panel h3{position:absolute;left:169px;top:128px;font-family:var(--serif);font-weight:400;font-size:29px;color:var(--white)}
.split-panel p{position:absolute;left:169px;top:178px;width:380px;font-size:14px;line-height:27px;color:var(--white)}

/* works */
.work{position:absolute;width:415px;height:301px}
.work .photo{position:absolute;left:0;top:0;width:415px;height:264px}
.work .label{position:absolute;left:0;top:229px;width:282px;height:72px;border-radius:0 36px 36px 0;padding:12px 0 0 26px;color:var(--white)}
.work .label b{display:block;font-family:var(--serif);font-weight:500;font-size:22px;line-height:26px}
.work .label small{font-size:13px}

/* stats */
.stats{left:0;top:2660px;width:1200px;height:244px;background:linear-gradient(180deg,#8db545,#78a23a)}
.stat{position:absolute;top:53px;width:220px;text-align:center;color:var(--white)}
.stat .ring{margin:0 auto;width:94px;height:94px;border-radius:50%;background:var(--white);border:3px solid var(--green);display:flex;align-items:center;justify-content:center;font-family:var(--serif);font-size:32px;color:var(--blue)}
.stat p{margin-top:14px;font-size:17px}

/* think green */
.green-photo{left:0;top:2906px;width:565px;height:515px;background:linear-gradient(180deg,#eef4e4,#dce9c6)}
.tg-title{left:661px;top:2970px;font-family:var(--serif);font-size:42px;color:var(--blue);font-weight:500}
.benefit{position:absolute;left:663px;display:flex;align-items:center;gap:26px}
.benefit .ic{width:72px;height:72px;border-radius:50%;background:#eef4e4;display:flex;align-items:center;justify-content:center}
.benefit b{display:block;font-family:var(--serif);font-weight:400;font-size:32px;color:var(--blue);line-height:34px}
.benefit span{font-family:var(--serif);font-size:23px;color:var(--ink)}

/* footer */
.footer{left:0;top:3641px;width:1200px;height:578px;background:linear-gradient(180deg,#2a2e29,#343a30)}
.cta{left:77px;top:3577px;width:1046px;height:113px;background:var(--green);border-radius:6px}
.cta p{position:absolute;left:51px;top:36px;font-family:var(--serif);font-size:30px;color:var(--white)}
.contact-ic{position:absolute;top:3980px;width:58px;height:58px;border-radius:50%;background:var(--green);display:flex;align-items:center;justify-content:center}
.contact-line{left:340px;top:4009px;width:510px;border-top:2px dotted rgba(165,207,76,.6)}
.contact-txt{position:absolute;top:4062px;width:300px;text-align:center;font-size:14px;line-height:27px;color:#b5b5b5}
.copy{left:0;top:4162px;width:1200px;text-align:center;font-size:13px;color:#b5b5b5}
.copy em{font-style:normal;color:var(--green)}
</style>
</head>
<body>

<header>
  <div class="abs topbar">
    <div class="social"><span class="s1"></span><span class="s2"></span><span class="s3"></span><span class="s4"></span><span class="s5"></span></div>
    <div class="call">Call Us On :
      <span class="ring"><svg width="16" height="16" viewBox="0 0 24 24"><path fill="#fff" d="M6.6 10.8a15 15 0 0 0 6.6 6.6l2.2-2.2c.3-.3.7-.4 1-.2 1.1.4 2.3.6 3.6.6.6 0 1 .4 1 1V20c0 .6-.4 1-1 1A17 17 0 0 1 3 4c0-.6.4-1 1-1h3.5c.6 0 1 .4 1 1 0 1.3.2 2.5.6 3.6.1.3 0 .7-.2 1z"/></svg></span>
      <b>555 014 2290</b></div>
  </div>
  <nav class="abs nav">
    <a class="active" style="left:371px">HOME</a>
    <a style="left:440px">ABOUT US</a>
    <div class="brand" style="left:530px;top:10px;width:140px"><span class="dot"></span><span class="name">CORVANE COLLECTIVE</span></div>
    <a style="left:689px">PROJECTS</a>
    <a style="left:788px">CONTACT</a>
  </nav>
</header>

<section class="abs hero" role="img" aria-label="Landscape photo contrasting green meadow and drought-cracked earth beneath a tree">
  <span class="arrow" style="left:12px"></span>
  <span class="arrow" style="right:12px"></span>
  <p class="kicker">Climate Adaptation</p>
  <h1>Implementing Climate Strategies</h1>
  <a class="btn btn-green" style="left:506px;top:352px;width:186px;height:56px">Contact Us</a>
</section>

<section>
  <h2 class="section-title" style="top:733px">What We Are Doing ?</h2>
  <div class="abs" style="left:303px;top:812px;width:594px;height:311px;background:linear-gradient(180deg,#8fa876,#6d8a4e)" role="img" aria-label="Family standing in front of a house with solar panels on the roof"></div>
  <p class="abs intro">Dedicated to taking action the Corvane Collective was created to help bring adaption strategies to life. Working with local communities we are committed to implementing strategies that will sustain communities throughout the Pacific Northwest for generations to come.</p>
  <a class="btn btn-green" style="left:506px;top:1278px;width:186px;height:55px">Learn More</a>
</section>

<section>
  <div class="abs split-photo" role="img" aria-label="Volunteers collecting litter along a wooded creek"></div>
  <div class="abs split-panel">
    <h3>On The ground…</h3>
    <p>The Collective is familiar and growing throughout the region. Presently our work has us on the ground in keystone watersheds in the Cascade, Willamette, Columbia and Boise basin watersheds.</p>
  </div>
  <div class="tab" style="top:1467px">Adaptation Plans</div>
  <div class="tab active" style="top:1534px">On The ground…</div>
  <div class="tab" style="top:1603px">Ecological Resilience</div>
  <div class="tab" style="top:1670px">Energy and Food</div>
</section>

<section>
  <h2 class="section-title" style="top:1878px">Recent Works</h2>
  <div class="work" style="left:174px;top:1960px">
    <div class="photo" style="background:linear-gradient(180deg,#9fb8b0,#7a9a66)" role="img" aria-label="Wind turbines and solar panels on green hills"></div>
    <div class="label" style="background:var(--green)"><b>Energy</b><small>investment in clean energy</small></div>
  </div>
  <div class="work" style="left:611px;top:1960px">
    <div class="photo" style="background:linear-gradient(180deg,#dcb878,#b98d4a)" role="img" aria-label="Close-up of ripe wheat ears"></div>
    <div class="label" style="background:var(--blue)"><b>Food Security</b><small>investment in clean energy</small></div>
  </div>
  <div class="work" style="left:174px;top:2292px">
    <div class="photo" style="background:linear-gradient(180deg,#8a5e3c,#6e5a3a)" role="img" aria-label="Aerial view of autumn forest valley with a river"></div>
    <div class="label" style="background:var(--blue)"><b>Ecological Resilience</b><small>Environmental Progress</small></div>
  </div>
  <div class="work" style="left:611px;top:2292px">
    <div class="photo" style="background:linear-gradient(180deg,#6f8160,#4f6640)" role="img" aria-label="Aerial view of a highway interchange surrounded by fields"></div>
    <div class="label" style="background:var(--blue)"><b>Infrastructure</b><small>Lorem ipsum</small></div>
  </div>
</section>

<section class="abs stats" role="img" aria-label="Background of a green field at sunset">
  <div class="stat" style="left:104px"><div class="ring">250+</div><p>Project Completed</p></div>
  <div class="stat" style="left:361px"><div class="ring">300+</div><p>Donations</p></div>
  <div class="stat" style="left:615px"><div class="ring">17+</div><p>Communities Engaged</p></div>
  <div class="stat" style="left:872px"><div class="ring">70+</div><p>Volunteers</p></div>
</section>

<section>
  <div class="abs green-photo" role="img" aria-label="Cupped hands holding a green globe among leaves"></div>
  <h2 class="abs tg-title">Think Green ! Save Money</h2>
  <div class="benefit" style="top:3037px"><span class="ic"><svg width="30" height="34" viewBox="0 0 30 34"><path d="M15 3C10 11 8 15 8 19a7 7 0 0 0 14 0c0-4-2-8-7-16z" fill="none" stroke="#4a7a2a" stroke-width="2"/><ellipse cx="15" cy="29" rx="11" ry="3" fill="none" stroke="#4a7a2a" stroke-width="2"/></svg></span><div><b>98%</b><span>Clean Water</span></div></div>
  <div class="benefit" style="top:3130px"><span class="ic"><svg width="30" height="34" viewBox="0 0 30 34"><path d="M15 32V6M15 12l-6-4M15 12l6-4M15 20l-6-4M15 20l6-4M15 28l-6-4M15 28l6-4" fill="none" stroke="#4a7a2a" stroke-width="2"/></svg></span><div><b>77%</b><span>Agriculture</span></div></div>
  <div class="benefit" style="top:3223px"><span class="ic"><svg width="34" height="34" viewBox="0 0 34 34"><circle cx="17" cy="13" r="9" fill="none" stroke="#4a7a2a" stroke-width="2"/><path d="M17 22v9M8 31h18" stroke="#4a7a2a" stroke-width="2"/></svg></span><div><b>56%</b><span>Forest Rescue</span></div></div>
  <div class="benefit" style="top:3317px"><span class="ic"><svg width="34" height="34" viewBox="0 0 34 34"><circle cx="17" cy="14" r="2" fill="#4a7a2a"/><path d="M17 14V3M17 14l9 6M17 14l-9 6M17 16v16" stroke="#4a7a2a" stroke-width="2" fill="none"/></svg></span><div><b>84%</b><span>Alternative energy</span></div></div>
  <a class="btn btn-blue" style="left:406px;top:3462px;width:187px;height:50px;font-size:18px">Join Us Today</a>
  <a class="btn btn-green" style="left:607px;top:3462px;width:187px;height:50px;font-size:18px">Contact Now</a>
</section>

<footer>
  <div class="abs footer" role="img" aria-label="Dark background of grasses at dusk"></div>
  <div class="abs cta">
    <p>If you have an any Question for Contact Us Today !</p>
    <a class="btn btn-blue" style="left:846px;top:33px;width:166px;height:49px;font-size:17px">Contact Us</a>
  </div>
  <div class="brand" style="left:450px;top:3752px;width:300px"><span class="dot" style="width:48px;height:48px"></span><span class="name" style="font-size:18px">CORVANE COLLECTIVE</span></div>
  <div class="social abs" style="left:482px;top:3898px"><span class="s1" style="width:38px;height:38px"></span><span class="s2" style="width:38px;height:38px;margin-left:10px"></span><span class="s3" style="width:38px;height:38px;margin-left:10px"></span><span class="s4" style="width:38px;height:38px;margin-left:10px"></span><span class="s5" style="width:38px;height:38px;margin-left:10px"></span></div>
  <div class="abs contact-line"></div>
  <span class="contact-ic" style="left:279px"><svg width="26" height="26" viewBox="0 0 24 24"><path fill="#fff" d="M6.6 10.8a15 15 0 0 0 6.6 6.6l2.2-2.2c.3-.3.7-.4 1-.2 1.1.4 2.3.6 3.6.6.6 0 1 .4 1 1V20c0 .6-.4 1-1 1A17 17 0 0 1 3 4c0-.6.4-1 1-1h3.5c.6 0 1 .4 1 1 0 1.3.2 2.5.6 3.6.1.3 0 .7-.2 1z"/></svg></span>
  <span class="contact-ic" style="left:571px"><svg width="24" height="28" viewBox="0 0 24 28"><path d="M12 1a9 9 0 0 0-9 9c0 7 9 17 9 17s9-10 9-17a9 9 0 0 0-9-9z" fill="#fff"/><circle cx="12" cy="10" r="3.5" fill="#a5cf4c"/></svg></span>
  <span class="contact-ic" style="left:850px"><svg width="26" height="20" viewBox="0 0 26 20"><rect x="1" y="1" width="24" height="18" rx="2" fill="#fff"/><path d="M2 3l11 8 11-8" fill="none" stroke="#a5cf4c" stroke-width="2"/></svg></span>
  <p class="contact-txt" style="left:157px">Phone:<br>555-018-4471</p>
  <p class="contact-txt" style="left:450px">418 Alder Ridge Rd,<br>Fernbrook WA 98001</p>
  <p class="contact-txt" style="left:737px">Email :<br>info@corvanecollective.org</p>
  <p class="abs copy">©<em>CORVANE COLLECTIVE</em> - 2020 All rights reserved.</p>
</footer>

</body>
</html>
```